We need a single web page design for a promotion. This page will acts as a landing page for users. Please provide us with a cutting edge design. I have attached a previous design used a couple of years ago.

Link: http://www.brightleafsnaps.com/bonuspack/
Updates

The Start Here box needs to look like this:

-Start Here (heading) 
-A box for email addresses to be entered
-Then a check box with "Yes, I have read and agree to the Privacy Policy and agree to receive email marketing from Bright Leaf Snaps and acknowledge that I will receive special email offers from our marketing partners, including the Ledger Post newsletter."
-A submit button 

All of this information needs to be in one box please.  And please feel free to contact me if you have any questions about this. 

Target Market(s)

Middle aged women (housewives)

Requirements
Must have
• Images must reflect the "500 Photo Prints". The only fields that are necessary are a box for email and a submit button.
Should not have
• The word FREE anywhere on the page

```html
<!DOCTYPE html>
<html lang="en">
<head>
<meta charset="utf-8">
<title>500 Photo Prints Delivered To You</title>
<link href="https://fonts.googleapis.com/css2?family=Questrial&family=Mulish:wght@800;900&family=Arimo:wght@400;700&display=swap" rel="stylesheet">
<style>
  :root {
    --navy-deep: #1f2d4d;
    --navy-band: #2f4a7d;
    --navy-panel: #3d5889;
    --navy-button: #1b2a49;
    --headline-dark: #16223c;
    --headline-soft: #2a3650;
    --sky-top: #5f9fd6;
    --sky-mid: #9cc7ea;
    --sky-low: #d4e7f5;
    --white: #ffffff;
    --field-text: #8a8f99;
    --panel-border: #e8eef6;
    --consent-text: #e3e9f3;
  }
  * { margin: 0; padding: 0; box-sizing: border-box; }
  html, body {
    width: 1200px;
    height: 646px;
    overflow: hidden;
    background: var(--white);
  }
  .page {
    position: relative;
    width: 1200px;
    height: 646px;
    overflow: hidden;
    font-family: "Arimo", Arial, sans-serif;
  }
  .top-band {
    position: absolute;
    left: 0; top: 0;
    width: 1200px; height: 13px;
    background: var(--navy-band);
  }
  .hero-scene {
    position: absolute;
    left: 0; top: 13px;
    width: 1200px; height: 569px;
    background:
      radial-gradient(ellipse 420px 300px at 1080px 470px, rgba(255,255,255,0.75), rgba(255,255,255,0) 70%),
      radial-gradient(ellipse 260px 120px at 1120px 60px, rgba(255,255,255,0.55), rgba(255,255,255,0) 70%),
      linear-gradient(180deg, var(--sky-top) 0%, var(--sky-mid) 45%, var(--sky-low) 100%);
  }
  .hero-photo {
    position: absolute;
    left: 0; top: 92px;
    width: 440px; height: 490px;
    background: linear-gradient(180deg, #c9d3dc 0%, #d9dfe4 50%, #eceff2 100%);
  }
  .headline {
    position: absolute;
    left: 591px; top: 80px;
    width: 520px;
    text-align: center;
    font-weight: normal;
  }
  .headline-lead {
    display: block;
    font-family: "Questrial", "Century Gothic", sans-serif;
    font-size: 42px;
    line-height: 48px;
    color: var(--headline-soft);
  }
  .headline-strong {
    display: block;
    font-family: "Mulish", "Century Gothic", sans-serif;
    font-weight: 900;
    font-size: 37px;
    line-height: 46px;
    letter-spacing: 0.5px;
    color: var(--headline-dark);
  }
  .signup-panel {
    position: absolute;
    left: 671px; top: 226px;
    width: 392px; height: 226px;
    border: 2px solid var(--panel-border);
    background: var(--navy-panel);
    box-shadow: 0 0 0 1px rgba(31,45,77,0.5);
  }
  .signup-product {
    position: absolute;
    left: 14px; top: 22px;
    width: 114px; height: 104px;
    background: linear-gradient(160deg, #e9eef4 0%, #8fb7d9 45%, #c9ced6 100%);
  }
  .signup-title {
    position: absolute;
    right: 20px; top: 12px;
    font-family: "Questrial", "Century Gothic", sans-serif;
    font-weight: normal;
    font-size: 23px;
    color: var(--white);
    letter-spacing: 0.5px;
  }
  .signup-email {
    position: absolute;
    left: 145px; top: 51px;
    width: 224px; height: 25px;
    border: 1px solid #c9d0db;
    background: var(--white);
    padding: 0 9px;
    font-family: "Arimo", Arial, sans-serif;
    font-size: 11px;
    color: var(--field-text);
  }
  .signup-email::placeholder { color: var(--field-text); }
  .signup-submit {
    position: absolute;
    left: 301px; top: 87px;
    width: 68px; height: 25px;
    border: none;
    background: var(--navy-button);
    color: var(--white);
    font-family: "Arimo", Arial, sans-serif;
    font-weight: 700;
    font-size: 11px;
    letter-spacing: 0.5px;
  }
  .signup-consent {
    position: absolute;
    left: 14px; top: 138px;
    width: 360px;
    display: flex;
    align-items: flex-start;
    gap: 7px;
    font-size: 9.5px;
    line-height: 12px;
    color: var(--consent-text);
  }
  .signup-consent input {
    flex: 0 0 auto;
    width: 11px; height: 11px;
    margin-top: 1px;
  }
  .signup-benefits {
    position: absolute;
    left: 0; bottom: 0;
    width: 100%; height: 26px;
    display: flex;
    align-items: center;
    justify-content: center;
    gap: 7px;
    font-size: 10px;
    color: var(--white);
    list-style: none;
    white-space: nowrap;
    background: rgba(27,42,73,0.35);
  }
  .offer-band {
    position: absolute;
    left: 0; top: 582px;
    width: 1200px; height: 27px;
    background: var(--navy-band);
    color: var(--white);
    font-size: 11.5px;
    letter-spacing: 0.4px;
    text-align: center;
    line-height: 27px;
  }
  .site-footer {
    position: absolute;
    left: 0; top: 609px;
    width: 1200px; height: 37px;
    background: var(--navy-deep);
    color: #d7dde8;
    font-size: 11.5px;
    text-align: center;
    line-height: 37px;
  }
  .site-footer a { color: #d7dde8; text-decoration: none; }
  .site-footer .divider { margin: 0 6px; }
</style>
</head>
<body>
<div class="page">
  <div class="top-band"></div>

  <div class="hero-scene" role="img" aria-label="Bright blue sky with soft white clouds"></div>
  <div class="hero-photo" role="img" aria-label="Photo of a woman in a white hooded parka looking up at the sky"></div>

  <h1 class="headline">
    <span class="headline-lead">Get 500 Photo Prints</span>
    <span class="headline-strong">DELIVERED TO YOU</span>
  </h1>

  <form class="signup-panel" action="http://www.brightleafsnaps.com/bonuspack/">
    <div class="signup-product" role="img" aria-label="Photo of a compact camera with a stack of printed photos"></div>
    <h2 class="signup-title">START HERE</h2>
    <input class="signup-email" type="email" placeholder="Enter Email here">
    <button class="signup-submit" type="submit">SUBMIT</button>
    <label class="signup-consent">
      <input type="checkbox" name="consent">
      <span>Yes, I have read and agree to the Privacy Policy and agree to receive email marketing from Bright Leaf Snaps and acknowledge that I will receive special email offers from our marketing partners, including the Ledger Post newsletter.</span>
    </label>
    <ul class="signup-benefits">
      <li>Professional Quality Photos</li>
      <li>|</li>
      <li>Unlimited storage</li>
      <li>|</li>
      <li>Share with Family &amp; Friends</li>
    </ul>
  </form>

  <div class="offer-band">*OFFER REDEMPTION WILL REQUIRE PARTICIPATION AND / OR PURCHASE OF THIRD PARTY OFFERS.</div>

  <footer class="site-footer">
    Copyright © 2011 All rights reserved. <a href="#">Privacy Policy</a><span class="divider">|</span><a href="#">Unsubscribe</a>
  </footer>
</div>
</body>
</html>
```